Harbor Crest Renewal Business Cards

We need a sleek and sexy business card design

Contact Information for Business Card

Name, address, phone number, email. Vincent Morrasco 482 Pellham Street Suite 200C Brookhollow NY 11958 (555)555-0174 Also a second version with the name Derek Halvorn

```html
<!DOCTYPE html>
<html lang="en">
<head>
<meta charset="utf-8">
<title>Harbor Crest Renewal – Business Cards</title>
<link rel="stylesheet" href="https://fonts.googleapis.com/css2?family=Montserrat:wght@400;600;700;800&display=swap">
<style>
  :root {
    --brand-blue: #17478a;
    --brand-red: #d2402a;
    --ink: #3a3a3a;
    --paper: #ffffff;
    --backdrop: #e6e7ea;
    --rule: #555555;
  }
  * { margin: 0; padding: 0; box-sizing: border-box; }
  html, body {
    width: 1200px; height: 895px; overflow: hidden;
    background: var(--backdrop);
    font-family: "Montserrat", sans-serif;
  }
  .canvas {
    position: relative; width: 1200px; height: 895px;
    display: flex; align-items: center; justify-content: center; gap: 40px;
  }
  .card {
    position: relative; width: 546px; height: 312px;
    box-shadow: 0 10px 28px rgba(0,0,0,.22);
  }
  .card--front {
    background: var(--brand-blue);
    display: flex; align-items: center; justify-content: center;
  }
  .wordmark {
    display: flex; align-items: center; gap: 12px;
    font-weight: 800; font-size: 30px; letter-spacing: .5px;
  }
  .wordmark__square { width: 26px; height: 26px; }
  .card--front .wordmark { color: var(--paper); }
  .card--front .wordmark__square { background: var(--paper); }
  .card--back { background: var(--paper); }
  .card--back .wordmark {
    position: absolute; left: 0; right: 0; top: 54px;
    justify-content: center; font-size: 26px; color: var(--brand-blue);
  }
  .card--back .wordmark__square { width: 22px; height: 22px; background: var(--brand-blue); }
  .address {
    position: absolute; left: 0; right: 0; top: 104px;
    text-align: center; color: var(--ink);
    font-size: 14px; line-height: 1.35; font-weight: 400;
  }
  .holder {
    position: absolute; left: 40px; top: 212px;
  }
  .holder__name {
    font-weight: 700; font-size: 21px; letter-spacing: .3px;
    color: var(--brand-blue); text-transform: uppercase;
  }
  .holder__name .surname { color: var(--brand-red); }
  .holder__title {
    font-size: 14px; color: var(--ink); margin-top: 2px; text-align: right;
  }
  .divider {
    position: absolute; left: 300px; top: 190px; width: 1px; height: 84px;
    background: var(--rule);
  }
  .contacts {
    position: absolute; left: 318px; top: 192px; list-style: none;
  }
  .contacts li {
    display: flex; align-items: center; gap: 10px;
    font-size: 13.5px; color: var(--ink); height: 27px;
  }
  .icon { width: 19px; height: 19px; flex: none; }
</style>
</head>
<body>
<main class="canvas">
  <section class="card card--front" aria-label="Card front">
    <div class="wordmark"><span class="wordmark__square"></span>Harbor Crest Renewal</div>
  </section>

  <section class="card card--back" aria-label="Card back">
    <div class="wordmark"><span class="wordmark__square"></span>Harbor Crest Renewal</div>
    <p class="address">482 Pellham Street Suite 200C<br>Brookhollow NY 11958</p>

    <div class="holder">
      <p class="holder__name">Vincent <span class="surname">Morrasco</span></p>
      <p class="holder__title">Founder &amp; CEO</p>
    </div>

    <div class="divider"></div>

    <ul class="contacts">
      <li>
        <svg class="icon" viewBox="0 0 20 20" aria-hidden="true">
          <circle cx="10" cy="10" r="9.5" fill="var(--brand-blue)"/>
          <path d="M7 5.5l1.6 2.2-1 1.1a7 7 0 0 0 3.6 3.6l1.1-1 2.2 1.6-.9 1.6c-4 .2-8-3.8-7.8-7.8z" fill="#fff"/>
        </svg>
        (555)555-0174
      </li>
      <li>
        <svg class="icon" viewBox="0 0 20 20" aria-hidden="true">
          <circle cx="10" cy="10" r="9.5" fill="var(--brand-red)"/>
          <rect x="5" y="6.5" width="10" height="7" fill="#fff"/>
          <path d="M5 6.5l5 4 5-4" fill="none" stroke="var(--brand-red)" stroke-width="1.1"/>
        </svg>
        info@yourdomain.com
      </li>
      <li>
        <svg class="icon" viewBox="0 0 20 20" aria-hidden="true">
          <circle cx="10" cy="10" r="9.5" fill="var(--brand-blue)"/>
          <g fill="none" stroke="#fff" stroke-width="1">
            <circle cx="10" cy="10" r="5"/>
            <ellipse cx="10" cy="10" rx="2.2" ry="5"/>
            <path d="M5 10h10M6 7.5h8M6 12.5h8"/>
          </g>
        </svg>
        yourdomain.com
      </li>
    </ul>
  </section>
</main>
</body>
</html>
```